Marketing Graphics for App

We need a feature graphic to be used in an app store listing for the app Quill Puzzles Plus. Quill Puzzles Plus is a brain training app that allows people to practice various cognitive skills. Our immediate need is for a graphic that can be scaled to run on the Verano Shop Hub free app of the day promotion. This ad will show up on the lock screen on the Tolvo Slate that users will see when the Tolvo Slate is turned on before it is unlocked.

We need a layered PSD file, so that internal elements can be scaled/moved. Please see the guidelines for the graphics ads from Verano.

Concept style guide: https://media-cdn.verano-example.com/docs/ads/VeranoLockCreativeRules.pdf

Technical style guide: https://media-cdn.verano-example.com/docs/ads/VeranoTolvoSlateAdGuide.pdf

I have included some of our existing graphics assets.

See also the app store listing:
http://www.verano-example.com/shop/item/Q77RTWPLMN

Target Market(s)

Mobile phone app users.

Industry/Entity Type

Training

Requirements
Must have
• Text: Quill Puzzles Plus

Text: Exercise Your Brain
Possibly add: Brain Training Games

```html
<!DOCTYPE html>
<html lang="en">
<head>
<meta charset="utf-8">
<title>Quill Puzzles Plus – Lock Screen Feature Graphic</title>
<link rel="stylesheet" href="https://fonts.googleapis.com/css2?family=Lato:wght@400;700;900&display=swap">
<style>
  :root {
    --page-bg: #f2f2f2;
    --status-bg: #0b0b0c;
    --status-text: #e6e6e6;
    --backdrop-navy: #27357e;
    --backdrop-pink: #c24d80;
    --backdrop-peach: #d99a86;
    --title-white: #ffffff;
    --tagline: rgba(235, 225, 235, 0.72);
    --pill-top: #4a4a4c;
    --pill-bottom: #202022;
    --pill-edge: #5d5d60;
    --pill-text: #ffffff;
    --knob-top: #6a6a6d;
    --knob-bottom: #3a3a3d;
  }
  * { margin: 0; padding: 0; box-sizing: border-box; }
  html, body {
    width: 1200px; height: 1200px; overflow: hidden;
    background: var(--page-bg);
    font-family: "Lato", Arial, sans-serif;
  }
  .lock-screen {
    position: absolute; left: 217px; top: 0;
    width: 766px; height: 1200px; overflow: hidden;
  }
  .status-bar {
    position: absolute; left: 0; top: 0; width: 100%; height: 34px;
    background: var(--status-bg); color: var(--status-text);
    font-size: 19px; font-weight: 400;
    display: flex; align-items: center; justify-content: space-between;
    padding: 0 22px 0 24px; z-index: 2;
  }
  .status-bar .clock { position: absolute; left: 50%; transform: translateX(-50%); }
  .status-icons { display: flex; gap: 12px; align-items: center; }
  .photo-backdrop {
    position: absolute; left: 0; top: 34px; width: 100%; height: 1166px;
    background: linear-gradient(170deg, var(--backdrop-navy) 0%, var(--backdrop-pink) 50%, var(--backdrop-peach) 100%);
  }
  .brand-mark {
    position: absolute; left: 236px; top: 295px;
    width: 330px; height: 330px; border-radius: 50%;
    background: var(--title-white);
  }
  .app-title {
    position: absolute; left: 0; width: 100%; top: 728px;
    text-align: center; color: var(--title-white);
    font-size: 55px; font-weight: 700; letter-spacing: 0.3px;
    white-space: nowrap;
  }
  .app-tagline {
    position: absolute; left: 0; width: 100%; top: 806px;
    text-align: center; color: var(--tagline);
    font-size: 25px; font-weight: 900; letter-spacing: 1px;
    text-transform: uppercase; white-space: nowrap;
  }
  .slider-pill {
    position: absolute; top: 966px; height: 107px;
    background: linear-gradient(180deg, var(--pill-top), var(--pill-bottom));
    border: 2px solid var(--pill-edge);
  }
  .start-pill {
    left: -2px; width: 197px;
    border-radius: 0 54px 54px 0;
    display: flex; align-items: center; padding-left: 40px;
    color: var(--pill-text); font-size: 19px; font-weight: 700;
    white-space: nowrap;
  }
  .unlock-pill {
    right: -2px; width: 199px; border-radius: 54px 0 0 54px;
  }
  .unlock-knob {
    position: absolute; left: 4px; top: 4px; width: 95px; height: 95px;
    border-radius: 50%;
    background: linear-gradient(180deg, var(--knob-top), var(--knob-bottom));
    box-shadow: 0 0 0 1px rgba(255,255,255,0.12);
    display: flex; align-items: center; justify-content: center;
  }
</style>
</head>
<body>
  <main class="lock-screen">
    <header class="status-bar">
      <span class="device-name">Lena's Tolvo</span>
      <span class="clock">9:28</span>
      <span class="status-icons">
        <svg class="wifi-icon" width="24" height="18" viewBox="0 0 24 18" aria-hidden="true">
          <path d="M2 6 A14 14 0 0 1 22 6" fill="none" stroke="#e6e6e6" stroke-width="2.4" stroke-linecap="round"/>
          <path d="M6 10 A8.5 8.5 0 0 1 18 10" fill="none" stroke="#e6e6e6" stroke-width="2.4" stroke-linecap="round"/>
          <circle cx="12" cy="14.5" r="2.4" fill="#e6e6e6"/>
        </svg>
        <svg class="battery-icon" width="30" height="14" viewBox="0 0 30 14" aria-hidden="true">
          <rect x="1" y="1" width="25" height="12" rx="2" fill="none" stroke="#e6e6e6" stroke-width="1.6"/>
          <rect x="3.5" y="3.5" width="20" height="7" fill="#e6e6e6"/>
          <rect x="27" y="4.5" width="2.5" height="5" fill="#e6e6e6"/>
        </svg>
      </span>
    </header>

    <div class="photo-backdrop" role="img" aria-label="Blurred bokeh light photograph in navy, pink, peach, cream and teal tones"></div>

    <div class="brand-mark" aria-hidden="true"></div>
    <h1 class="app-title">Quill Puzzles Plus</h1>
    <p class="app-tagline">Exercise Your Brain</p>

    <div class="slider-pill start-pill">Start Now</div>
    <div class="slider-pill unlock-pill">
      <div class="unlock-knob">
        <svg class="lock-icon" width="26" height="32" viewBox="0 0 26 32" aria-label="Unlock">
          <path d="M6 14 V9 A7 7 0 0 1 20 9 V14" fill="none" stroke="#d8d8d8" stroke-width="3"/>
          <rect x="2" y="13" width="22" height="17" rx="3" fill="#d8d8d8"/>
          <circle cx="13" cy="20.5" r="2.4" fill="#3a3a3d"/>
          <rect x="12" y="21" width="2" height="5" fill="#3a3a3d"/>
        </svg>
      </div>
    </div>
  </main>
</body>
</html>
```